Site for a workout and Consulting enterprise

I need a professional responsive site for www.valomer.hamburg. The website shoulderstand consist of a Landing and 4 other pages. - On page for the contact informations - on page for the about - on page for consulting services (technical) - on page for Training and workshop services (business and soft skills) I add some files so you can see my idea of the design.
Target Market(s)
IT and Management
Industry/Entity Type
Management Consulting
Coding
Coded - Design and coding required
Number of Pages Required
4 page
Requirements
Must have
- Use Pictures for Background, Sliders and Topics. Just have to placeholders for the design.

```html
<!DOCTYPE html>
<html lang="en">
<head>
<meta charset="utf-8">
<title>valomer – Training &amp; Consulting</title>
<link rel="stylesheet" href="https://fonts.googleapis.com/css2?family=Open+Sans:wght@400;800&family=Oswald:wght@400;500&display=swap">
<style>
  :root {
    --brand-blue-light: #3f6f91;
    --brand-blue-dark: #1f4a6a;
    --photo-dark: #2a2520;
    --photo-mid: #3b342c;
    --white: #ffffff;
    --footer-bg: #ffffff;
    --footer-text: #555555;
  }
  * { margin: 0; padding: 0; box-sizing: border-box; }
  html, body { width: 1200px; height: 716px; overflow: hidden; }
  body { position: relative; font-family: "Open Sans", sans-serif; background: var(--footer-bg); }

  .brand-panel {
    position: absolute; left: 0; top: 0; width: 600px; height: 665px;
    background: radial-gradient(ellipse at 45% 48%, var(--brand-blue-light) 0%, var(--brand-blue-dark) 75%);
    display: flex; align-items: center; justify-content: center;
  }
  .brand-name {
    font-family: "Open Sans", sans-serif; font-weight: 800; font-size: 78px;
    color: var(--white); letter-spacing: -2px; margin-top: -4px;
  }

  .services-panel {
    position: absolute; left: 600px; top: 0; width: 600px; height: 665px;
    background: linear-gradient(160deg, var(--photo-mid) 0%, var(--photo-dark) 55%, var(--photo-mid) 100%);
  }

  .service { position: absolute; color: var(--white); }
  .service-icon {
    position: absolute; width: 68px; height: 68px; border: 1.5px solid var(--white);
    border-radius: 50%; display: flex; align-items: center; justify-content: center;
  }
  .service-title {
    position: absolute; font-family: "Oswald", sans-serif; font-weight: 500;
    font-size: 23px; line-height: 1; white-space: nowrap;
  }
  .service-text {
    position: absolute; font-size: 12.5px; line-height: 25px; width: 210px;
  }

  .expand-button {
    position: absolute; left: 644px; top: 299px; width: 66px; height: 66px;
    border: 2px solid var(--white); border-radius: 50%;
    display: flex; align-items: center; justify-content: center;
  }

  .main-nav { position: absolute; right: 32px; top: 604px; display: flex; gap: 40px; }
  .main-nav a {
    font-family: "Oswald", sans-serif; font-size: 24px; color: var(--white);
    text-decoration: none; text-transform: uppercase;
  }

  .site-footer {
    position: absolute; left: 0; top: 665px; width: 1200px; height: 51px;
    display: flex; align-items: center; justify-content: space-between;
    padding: 0 60px 0 33px; font-size: 11.5px; color: var(--footer-text);
  }
  .social { display: flex; align-items: center; gap: 24px; }
  .social-label { margin-right: 2px; }
  .social-dot { width: 10px; height: 10px; border-radius: 50%; display: inline-block; }
  .dot-1 { background: #3b5998; }
  .dot-2 { background: #1da1f2; }
  .dot-3 { background: #dd4b39; }
  .dot-4 { background: #cb2027; }
  .dot-5 { background: #0077b5; }
</style>
</head>
<body>
  <section class="brand-panel">
    <div class="brand-name">valomer</div>
  </section>

  <section class="services-panel" role="img" aria-label="Dark photo of hands arranging wooden blocks and puzzle pieces on a wooden table, with a light bulb sketch"></section>

  <article class="service" style="left:718px; top:139px;">
    <div class="service-icon" style="left:0; top:0;">
      <svg width="36" height="30" viewBox="0 0 36 30" fill="none" stroke="#fff" stroke-width="1.3">
        <rect x="10" y="2" width="24" height="16"/>
        <circle cx="6" cy="10" r="3"/>
        <path d="M1 28v-8a4 4 0 0 1 4-4h3l8-5"/>
        <path d="M8 28v-8"/>
      </svg>
    </div>
    <h2 class="service-title" style="left:94px; top:0;">Training</h2>
    <p class="service-text" style="left:94px; top:36px;">Lorem Ipsum is simply dummy text of the printing and typesetting&nbsp; has been the industry...</p>
  </article>

  <div class="expand-button">
    <svg width="30" height="30" viewBox="0 0 30 30" stroke="#fff" stroke-width="2"><path d="M15 1v28M1 15h28"/></svg>
  </div>

  <article class="service" style="left:773px; top:296px;">
    <div class="service-icon" style="left:0; top:0;">
      <svg width="36" height="28" viewBox="0 0 36 28" fill="none" stroke="#fff" stroke-width="1.3">
        <path d="M12 2h22v14h-5l-3 4v-4h-4"/>
        <path d="M2 8h20v14H9l-4 4v-4H2z"/>
      </svg>
    </div>
    <h2 class="service-title" style="left:93px; top:10px;">Consulting</h2>
    <p class="service-text" style="left:93px; top:46px;">Lorem Ipsum is simply dummy text of the printing and typesetting&nbsp; has been the industry...</p>
  </article>

  <article class="service" style="left:718px; top:439px;">
    <div class="service-icon" style="left:0; top:0;">
      <svg width="34" height="34" viewBox="0 0 34 34" fill="none" stroke="#fff" stroke-width="1.3">
        <path d="M4 10h8a4 4 0 1 1 8 0h8v8a4 4 0 1 0 0 8v6h-8a4 4 0 1 0-8 0H4v-8a4 4 0 1 1 0-8z"/>
      </svg>
    </div>
    <h2 class="service-title" style="left:94px; top:0;">Solution</h2>
    <p class="service-text" style="left:94px; top:36px;">Lorem Ipsum is simply dummy text of the printing and typesetting&nbsp; has been the industry...</p>
  </article>

  <nav class="main-nav">
    <a href="#impressum">Impressum</a>
    <a href="#kontakt">Kontakt</a>
  </nav>

  <footer class="site-footer">
    <span>© 2017. valomer. All rights reserved.</span>
    <div class="social">
      <span class="social-label">Connect with our social nwtwork :</span>
      <span class="social-dot dot-1"></span>
      <span class="social-dot dot-2"></span>
      <span class="social-dot dot-3"></span>
      <span class="social-dot dot-4"></span>
      <span class="social-dot dot-5"></span>
    </div>
  </footer>
</body>
</html>
```